Business Card Design Project

Logo, Phone Number, slogan, must be included on front of card. Services must be listed: Lawn Service, Fertilization, Pool Service, Pressure Washing. and a space to "write in" salesmans name.
Slogan "Your Everything Outside Company"
Phone: 555-204-3816
Email: brightmeadowgroup@mailvane.com
Looking for a bold yet simple design to enforce brand recognition.

Target Market(s)

Middle to upper class US homeowners

Industry/Entity Type

Business

Requirements
Must have
• Logo, Phone, and Slogan on front
Should not have
• cluttered background

```html
<!DOCTYPE html>
<html lang="en">
<head>
<meta charset="utf-8">
<title>Bright Meadow Services – Business Card</title>
<link rel="stylesheet" href="https://fonts.googleapis.com/css2?family=Arimo:wght@400;700&family=Open+Sans:wght@400;600&display=swap">
<style>
  :root {
    --ink: #111111;
    --card-black: #121212;
    --paper: #ffffff;
    --brand-blue: #1569c7;
    --leaf-green: #6aa63a;
    --rule: #3a3a3a;
    --gap: #ececec;
  }
  * { margin: 0; padding: 0; box-sizing: border-box; }
  html, body { width: 1040px; height: 1200px; overflow: hidden; background: var(--gap); }
  .sheet { position: relative; width: 1040px; height: 1200px; }

  .card { position: absolute; left: 0; width: 1040px; overflow: hidden; }
  .card--front { top: 0; height: 622px; background: var(--paper); }
  .card--back { top: 632px; height: 568px; background: var(--card-black); }

  .front-panel { position: absolute; inset: 0; }

  .salesman-name {
    position: absolute; left: 97px; top: 140px;
    font-family: "Open Sans", sans-serif; font-size: 39px; color: var(--paper);
  }
  .salesman-title {
    position: absolute; left: 247px; top: 214px;
    font-family: "Open Sans", sans-serif; font-size: 30px; color: var(--leaf-green);
  }
  .contact {
    position: absolute; right: 590px;
    font-family: "Open Sans", sans-serif; color: var(--paper); text-align: right;
  }
  .contact--phone { top: 390px; font-size: 35px; right: 630px; }
  .contact--email { top: 488px; font-size: 24px; right: 592px; }

  .brand-name {
    position: absolute; font-family: "Arimo", sans-serif; font-weight: 700;
    color: var(--brand-blue); line-height: 1.02; letter-spacing: 1px;
    display: flex; align-items: center; gap: 18px;
  }
  .brand-name__mark { width: 34px; height: 34px; background: var(--brand-blue); flex: none; }
  .brand-name--front { left: 636px; top: 80px; font-size: 58px; }
  .brand-name--back { left: 92px; top: 230px; font-size: 54px; }

  .slogan {
    position: absolute; left: 610px; top: 303px; width: 430px; height: 139px;
    background: var(--brand-blue); color: var(--ink);
    font-family: "Arimo", sans-serif; font-size: 39px; line-height: 1.05;
    display: flex; align-items: center; justify-content: center; text-align: center;
  }

  .services {
    position: absolute; left: 558px; top: 208px; width: 482px; height: 192px;
    background: var(--brand-blue); color: var(--ink);
    font-family: "Arimo", sans-serif; padding: 12px 0 0 36px;
  }
  .services__title { font-size: 37px; font-weight: 400; line-height: 1; margin-bottom: 2px; }
  .services__list { list-style: none; font-size: 30px; line-height: 1.02; padding-left: 0; }
  .services__list li::before { content: "* "; }
</style>
</head>
<body>
<div class="sheet">

  <section class="card card--front">
    <svg class="front-panel" width="1040" height="622" viewBox="0 0 1040 622">
      <polygon points="0,0 430,0 592,622 0,622" fill="var(--card-black)"/>
      <line x1="95" y1="368" x2="436" y2="368" stroke="var(--rule)" stroke-width="2"/>
      <line x1="95" y1="460" x2="458" y2="460" stroke="var(--rule)" stroke-width="2"/>
      <line x1="95" y1="553" x2="580" y2="553" stroke="var(--rule)" stroke-width="2"/>
      <polygon points="435,369 527,369 550,458 458,458" fill="var(--brand-blue)"/>
      <polygon points="460,462 552,462 575,552 483,552" fill="var(--brand-blue)"/>
      <g class="icon-phone" fill="#fff">
        <path d="M474 406 q18 -12 36 0 l0 7 l-8 0 l-2 -5 q-8 -3 -16 0 l-2 5 l-8 0 z"/>
        <rect x="478" y="414" width="28" height="14" rx="2"/>
      </g>
      <g class="icon-monitor" fill="none" stroke="#fff" stroke-width="4">
        <rect x="497" y="492" width="34" height="24"/>
        <line x1="514" y1="516" x2="514" y2="524"/>
        <line x1="504" y1="526" x2="524" y2="526"/>
      </g>
    </svg>

    <p class="salesman-name">write in name ...</p>
    <p class="salesman-title">Salesman</p>
    <p class="contact contact--phone">555-204-3816</p>
    <p class="contact contact--email">brightmeadowgroup@mailvane.com</p>

    <div class="brand-name brand-name--front">
      <span class="brand-name__mark"></span>
      <span>BRIGHT<br>MEADOW</span>
    </div>

    <div class="slogan">"Your Everything<br>Outside Company"</div>
  </section>

  <section class="card card--back">
    <div class="brand-name brand-name--back">
      <span class="brand-name__mark"></span>
      <span>BRIGHT<br>MEADOW</span>
    </div>

    <div class="services">
      <h2 class="services__title">Services</h2>
      <ul class="services__list">
        <li>Fertilization</li>
        <li>Pool Service</li>
        <li>Pressure Washing</li>
        <li>Lawn Service</li>
      </ul>
    </div>
  </section>

</div>
</body>
</html>
```